Unique Home Cooking School needs Wordpress Design

We need a wordpress design for our small business based in Singapore called Brisk Ladles. It is a unique cooking school where the cooking course menu is completely customised to our client's preference/lifestyle/requests. More information can be found on our site: briskladles.example

We are looking for something simple and easy to navigate. We are currently using a free template which we have customised ourselves. As the business is growing, we are looking to have a site more suited to our needs. The site should also be photo friendly, as we often post up photos of our food. It should also be social media integrated as a lot of our business is driven by PQ.

The look and feel should really reflect the personalities of both owners - like the logo. Please feel free to contact us if you need more clarification.

Target Market(s)

Our target audience are usually female, with children, aged 25 - 45.
They are either stay-at-home mums or full-time mums that are keen to do more for the family.

Industry/Entity Type

Small Business

Requirements
Must have
• The wordpress design has to be able to accommodate food photos on every page.
It also needs to be able to support social media feeds within the site.
Should not have
• Design should not have any chef-like design elements as we are not chefs. We are two stay-home-mums wanting to impart skills to other stay-home-mums or domestic helpers.

```html
<!DOCTYPE html>
<html lang="en">
<head>
<meta charset="utf-8">
<title>Brisk Ladles – Home Cooking School</title>
<link rel="stylesheet" href="https://fonts.googleapis.com/css2?family=Raleway:wght@400;600;700&family=Lato:wght@400;700&display=swap">
<style>
:root{
  --page:#ffffff;
  --ink:#2b2b2b;
  --muted:#8a8a8a;
  --soft:#b5b5b5;
  --accent:#e45fbf;
  --dark:#25282a;
  --darker:#2e3134;
  --line:#d9d9d9;
  --green:#4caf50;
  --red:#d9534f;
}
*{box-sizing:border-box;margin:0;padding:0}
html,body{width:669px;height:1200px;overflow:hidden;background:var(--page)}
body{font-family:"Lato",sans-serif;color:var(--ink);position:relative}
.abs{position:absolute}
.photo{position:absolute}
h1,h2,h3,h4{font-family:"Raleway",sans-serif}

/* hero */
.hero{left:137px;top:0;width:395px;height:200px;background:linear-gradient(135deg,#6c7177 0%,#50565c 45%,#3e4348 100%)}
.hero-bulbs{left:137px;top:0;width:150px;height:170px;background:radial-gradient(ellipse at 40% 35%,#f1eee8 0%,#d8d3ca 40%,rgba(90,95,100,0) 72%)}
.hero-kicker{left:343px;top:60px;font-size:5.5px;letter-spacing:1.5px;color:#e8e8e8;text-transform:uppercase}
.hero-title{left:342px;top:66px;font-size:19px;font-weight:600;color:#fff}
.hero-text{left:343px;top:97px;width:160px;font-size:5.5px;line-height:8px;color:#eee}
.btn-ghost{left:343px;top:128px;width:49px;height:14px;border:1px solid #fff;color:#fff;font-size:4.5px;font-weight:700;letter-spacing:.6px;display:flex;align-items:center;justify-content:center;font-family:"Raleway",sans-serif}

/* nav */
.brand{left:163px;top:207px;display:flex;align-items:center;gap:4px}
.brand-mark{width:9px;height:9px;border-radius:50%;background:var(--ink)}
.brand-name{font-family:"Raleway",sans-serif;font-weight:700;font-size:9px;color:var(--ink)}
.nav{left:322px;top:214px;display:flex;gap:0}
.nav-item{width:32px;text-align:center;font-family:"Raleway",sans-serif;font-size:4.3px;font-weight:700;letter-spacing:.4px;color:#333}
.nav-item svg{display:block;margin:0 auto 4px;width:9px;height:9px;fill:#333}
.nav-item.is-active{color:var(--accent)}
.nav-item.is-active svg{fill:var(--accent)}

/* feature columns */
.feature-img{top:276px;width:110px;height:68px}
.feature-title{top:352px;font-family:"Raleway",sans-serif;font-size:5.2px;font-weight:700;letter-spacing:.4px}
.feature-sub{top:360px;font-size:5.6px;color:var(--muted)}
.feature-text{top:372px;width:110px;font-size:4.2px;line-height:6.6px;color:var(--soft)}

/* band */
.band{left:137px;top:408px;width:395px;height:140px;background:radial-gradient(ellipse at 50% 75%,#7a4a30 0%,#3a2a22 45%,#1f1d1c 100%)}
.band-icon{left:327px;top:440px;width:15px;height:18px}
.band-title{left:137px;top:473px;width:395px;text-align:center;font-size:19px;font-weight:600;letter-spacing:1px;color:#fff}
.band-quote{left:210px;top:506px;width:250px;text-align:center;font-size:6.6px;line-height:12px;color:#ddd;font-style:italic}

/* split sections */
.sec-title{font-size:9.5px;font-weight:600;letter-spacing:.6px}
.sec-sub{font-size:7px;color:var(--soft)}
.sec-rule{width:14px;height:1px;background:var(--ink)}
.sec-text{width:170px;font-size:4.6px;line-height:7.5px;color:#555}
.btn-outline{height:14px;border:1px solid #333;font-family:"Raleway",sans-serif;font-size:4.6px;font-weight:700;letter-spacing:.6px;display:flex;align-items:center;justify-content:center}

/* info columns */
.col-head{top:873px;font-family:"Raleway",sans-serif;font-size:5.6px;font-weight:600}
.col-rule{top:882px;height:1px;background:var(--line)}
.col-text{font-size:4.2px;line-height:6.7px;color:#666}
.hours{left:155px;top:924px;list-style:none;font-size:4.2px;line-height:7px;color:#555}
.hours li{display:flex;align-items:center;gap:3px}
.hours i{width:4px;height:4px;border-radius:50%;border:1px solid var(--green)}
.hours li.closed i{border-color:var(--red)}
.btn-dark{left:248px;top:942px;width:57px;height:13px;background:var(--dark);color:#fff;font-family:"Raleway",sans-serif;font-size:4.2px;font-weight:700;letter-spacing:.4px;display:flex;align-items:center;justify-content:center}
.gallery{left:341px;top:891px;width:172px;height:66px;display:grid;grid-template-columns:repeat(4,1fr);grid-template-rows:repeat(2,1fr);gap:1px}
.gallery span{display:block}

/* reviews */
.reviews{left:137px;top:969px;width:395px;height:99px;background:linear-gradient(90deg,#3b3f42 0%,#4a4e51 55%,#5a2a33 80%,#43474a 100%)}
.reviews-title{left:156px;top:995px;font-size:8px;font-weight:600;letter-spacing:.8px;color:#fff}
.reviews-quote{left:156px;top:1024px;width:205px;font-size:5.6px;line-height:10px;color:#eee;font-style:italic}
.reviews-name{left:156px;top:1051px;font-size:4px;font-weight:700;color:#fff}
.reviews-stars{left:156px;top:1058px;font-size:5px;color:#fff;letter-spacing:.5px}
.dots{left:347px;top:1053px;display:flex;gap:2px}
.dots i{width:4px;height:4px;border-radius:50%;border:1px solid #fff}
.dots i.on{background:#fff}

/* call to action */
.cta{left:137px;top:1068px;width:395px;height:80px;background:var(--dark)}
.cta-text{left:137px;top:1095px;width:395px;text-align:center;font-family:"Raleway",sans-serif;font-size:9px;font-weight:700;line-height:15px;letter-spacing:.6px;color:#fff}
.cta-rule{left:328px;top:1132px;width:13px;height:1px;background:#888}

/* footer */
.footer{left:137px;top:1148px;width:395px;height:52px;background:var(--darker)}
.footer-copy{left:157px;top:1172px;font-size:3.8px;line-height:6.5px;color:#7d8185}
.social{left:425px;top:1174px;display:flex;gap:5px}
.social i{width:4px;height:4px;border-radius:50%;background:#6d7175}
.to-top{left:513px;top:1179px;width:10px;height:10px;border-radius:50%;background:#1c1e20}
</style>
</head>
<body>

<!-- Hero -->
<div class="abs hero" role="img" aria-label="Garlic bulbs and cloves on a weathered grey wooden table"></div>
<div class="abs hero-bulbs" role="img" aria-label="Garlic bulbs in close-up"></div>
<p class="abs hero-kicker">Finger lickin' good</p>
<h1 class="abs hero-title">Delicious Recipes</h1>
<p class="abs hero-text">Welcome to the Home of Fabulously Tasty homemade food that's gonna make you forget your mom.</p>
<a class="abs btn-ghost">LEARN MORE &nbsp;›</a>

<!-- Header -->
<div class="abs brand"><span class="brand-mark"></span><span class="brand-name">Brisk Ladles</span></div>
<nav class="abs nav">
  <a class="nav-item is-active"><svg viewBox="0 0 10 10"><path d="M5 1 1 5h1.3v4h2.2V6.5h1V9h2.2V5H9z"/></svg>HOME</a>
  <a class="nav-item"><svg viewBox="0 0 10 10"><path d="M2 1h4l2 2v6H2zM3 5h4v.8H3zm0 1.6h4v.8H3z" fill-rule="evenodd"/></svg>COURSES</a>
  <a class="nav-item"><svg viewBox="0 0 10 10"><path d="M1 2h8v6H1zm1 5h6L6 4.5 4.5 6 3.5 5z"/></svg>GALLERY</a>
  <a class="nav-item"><svg viewBox="0 0 10 10"><path d="m5 .8 1.3 2.7 3 .4-2.2 2.1.5 3L5 7.6 2.4 9l.5-3L.7 3.9l3-.4z"/></svg>REVIEWS</a>
  <a class="nav-item"><svg viewBox="0 0 10 10"><path d="M7 1 9 3 4 8H2V6zM1.5 9h7v.6h-7z"/></svg>BLOG</a>
  <a class="nav-item"><svg viewBox="0 0 10 10"><path d="M5 .8a3 3 0 0 0-3 3C2 6 5 9.5 5 9.5S8 6 8 3.8a3 3 0 0 0-3-3zm0 4.2a1.2 1.2 0 1 1 0-2.4 1.2 1.2 0 0 1 0 2.4z"/></svg>CONTACT</a>
</nav>

<!-- Feature columns -->
<div class="photo feature-img" style="left:155px;background:radial-gradient(circle at 50% 50%,#9fd04a 0 18%,#eef0e6 19% 28%,#6b4a30 30%,#3a271a 100%)" role="img" aria-label="Empty green plate with knife and fork on a wooden table"></div>
<div class="photo feature-img" style="left:279px;background:linear-gradient(180deg,#5a1515 0%,#2a0c0c 100%)" role="img" aria-label="Diners seated at a restaurant table in red light"></div>
<div class="photo feature-img" style="left:402px;background:radial-gradient(ellipse at 50% 55%,#f3efe6 0 30%,#a06a3a 45%,#6a4124 100%)" role="img" aria-label="Slice of cake on a white plate"></div>

<h3 class="abs feature-title" style="left:155px">WHY CHOOSE US.</h3>
<p class="abs feature-sub" style="left:155px">Because we are Reliable</p>
<p class="abs feature-text" style="left:155px">Lorem ipsum dolor sit amet, consectetur adipisicing elit. Eligendi non facilis sed voluptatum sunt voluptatem accusamus molestiae neque perspiciatis mollitia.</p>

<h3 class="abs feature-title" style="left:279px">OUR MISSION.</h3>
<p class="abs feature-sub" style="left:279px">To Redefine your Brand.</p>
<p class="abs feature-text" style="left:279px">Quos, non, esse eligendi ab accusantium voluptatem. Maxime eligendi beatae, atque tempora culpa. Vitae debitis quia, consequatur rerum molestiae quo.</p>

<h3 class="abs feature-title" style="left:402px">WHAT WE DO.</h3>
<p class="abs feature-sub" style="left:402px">Make our Customers Happy.</p>
<p class="abs feature-text" style="left:402px">Porro repellat vero sapiente amet vitae quibusdam necessitatibus consectetur labore totam. Accusamus perspiciatis asperiores labore esse ab accusamus modi ut.</p>

<!-- Teachers band -->
<div class="abs band" role="img" aria-label="Hands serving a steaming roasted dish on a dark table"></div>
<svg class="abs band-icon" viewBox="0 0 15 18" fill="#fff" aria-hidden="true">
  <path d="M1 0h1v6h1V0h1v6h1V0h1v7a2 2 0 0 1-2 2v9H3V9a2 2 0 0 1-2-2zM10 0c3 0 4 4 4 8h-2v10h-2z"/>
</svg>
<h2 class="abs band-title">BRILLIANT TEACHERS</h2>
<p class="abs band-quote">“Momentum poverty tackling fellows social impact. Expanding community ownership, future affiliate protect civil society. Northwind.”</p>

<!-- Fresh from the garden -->
<div class="photo" style="left:160px;top:572px;width:165px;height:82px;background:radial-gradient(ellipse at 50% 55%,#d8432a 0%,#7fae3a 40%,#ffffff 72%)" role="img" aria-label="Pile of fresh vegetables: peppers, cabbage, tomatoes and greens"></div>
<h2 class="abs sec-title" style="left:343px;top:571px">FRESH FROM THE GARDEN.</h2>
<p class="abs sec-sub" style="left:343px;top:588px">Duis mollis, est non commodo luctus. Donec sed odio dui</p>
<div class="abs sec-rule" style="left:343px;top:606px"></div>
<p class="abs sec-text" style="left:343px;top:622px">Lorem ipsum dolor sit amet, consectetur adipisicing elit. Molestiae, repudiandae, maxime, earum, sapiente assumenda non elit laborum qui vero vel quos sint excepturi in laudantium.</p>
<a class="abs btn-outline" style="left:343px;top:667px;width:55px">VIEW RECIPES</a>

<!-- You'll be lovin' it -->
<h2 class="abs sec-title" style="left:155px;top:732px">YOU'LL BE LOVIN' IT.</h2>
<p class="abs sec-sub" style="left:155px;top:747px">Duis mollis, est non commodo luctus. Donec sed odio dui</p>
<div class="abs sec-rule" style="left:155px;top:766px"></div>
<p class="abs sec-text" style="left:155px;top:781px">Lorem ipsum dolor sit amet, consectetur adipisicing elit. Molestiae, repudiandae, maxime, earum, sapiente assumenda non elit laborum qui vero vel quos sint excepturi in laudantium.</p>
<a class="abs btn-outline" style="left:155px;top:826px;width:58px">MORE DETAILS</a>
<div class="photo" style="left:340px;top:734px;width:172px;height:64px;background:radial-gradient(ellipse at 60% 55%,#c98a3a 0%,#8a5a2a 35%,#ffffff 70%)" role="img" aria-label="Row of burgers on a white background"></div>

<!-- Info columns -->
<h4 class="abs col-head" style="left:155px">Opening Hours</h4>
<div class="abs col-rule" style="left:155px;width:80px"></div>
<p class="abs col-text" style="left:155px;top:892px;width:82px">Lorem ipsum dolor sit amet, consectetur adipisicing elit. Aperiam aspernatur facilis cumque amet suscipit odio.</p>
<ul class="abs hours">
  <li><i></i><b>Mondays-Fridays:</b>&nbsp;10AM to 7PM</li>
  <li><i></i><b>Saturdays:</b>&nbsp;11AM to 3PM</li>
  <li class="closed"><i></i><b>Sundays:</b>&nbsp;Closed</li>
</ul>

<h4 class="abs col-head" style="left:248px">Our Course Menu</h4>
<div class="abs col-rule" style="left:248px;width:80px"></div>
<p class="abs col-text" style="left:248px;top:892px;width:75px">Our Course Menu is unique &amp; filling consisting of different types of 5 Starters, 12 Full-Course Dishes, 9 Desserts &amp; 3 Mocktails which you are gonna relish to the core.</p>
<a class="abs btn-dark">▤&nbsp; BROWSE MENU</a>

<h4 class="abs col-head" style="left:341px">Gallery</h4>
<div class="abs col-rule" style="left:341px;width:172px"></div>
<div class="abs gallery" role="img" aria-label="Grid of eight food photos: plates, dishes, tomatoes and garlic">
  <span style="background:#3f4a3a"></span><span style="background:#b7803e"></span><span style="background:#5a5f64"></span><span style="background:#8a3a2a"></span>
  <span style="background:#6c7075"></span><span style="background:#4a4f54"></span><span style="background:#55504a"></span><span style="background:#a98a80"></span>
</div>

<!-- Reviews -->
<div class="abs reviews" role="img" aria-label="Red chili pepper on a dark wooden surface"></div>
<h2 class="abs reviews-title">REVIEWS</h2>
<p class="abs reviews-quote">“Medicine, experience in the field climate change achieve voice public-private partnerships process our ambitions. Sanitation.”</p>
<p class="abs reviews-name">Lena Ortiz, Harbor Daily</p>
<p class="abs reviews-stars">★★★★☆</p>
<div class="abs dots"><i></i><i class="on"></i><i></i></div>

<!-- Call to action -->
<div class="abs cta"></div>
<p class="abs cta-text">NEED TO JOIN US TO LEARN ABOUT AWESOME COOKING ? CALL<br>+123.5550.0199</p>
<div class="abs cta-rule"></div>

<!-- Footer -->
<div class="abs footer"></div>
<p class="abs footer-copy">Copyright © 2015 All Rights Reserved<br>Terms of Use • Privacy Policy</p>
<div class="abs social"><i></i><i></i><i></i><i></i><i></i><i></i><i></i><i></i></div>
<svg class="abs to-top" viewBox="0 0 10 10" aria-label="Back to top"><circle cx="5" cy="5" r="5" fill="#1c1e20"/><path d="M3 6 5 4l2 2" stroke="#fff" stroke-width=".9" fill="none"/></svg>

</body>
</html>
```